" Especializada em projetos de arquitetura e interiores de residências e espaços comerciais, serviços de reforma e obra civil ; execuçao de movelaria personalizada. "

```html
<!DOCTYPE html>
<html lang="pt-BR">
<head>
<meta charset="utf-8">
<title>Lar Traço – Cartão de visita</title>
<link rel="stylesheet" href="https://fonts.googleapis.com/css2?family=Questrial&family=Lato:wght@400&display=swap">
<style>
  :root {
    --backdrop: #8f8f8f;
    --card-dark: #1f1f1f;
    --card-light: #ffffff;
    --ink: #1a1a1a;
    --ink-soft: #3a3a3a;
    --accent-light: #f2f2f2;
    --deco-top: #5a5a5a;
    --deco-bottom: #2a2a2a;
  }
  html, body {
    margin: 0;
    padding: 0;
    width: 1200px;
    height: 1200px;
    overflow: hidden;
    background: var(--backdrop);
  }
  .canvas {
    position: relative;
    width: 1200px;
    height: 1200px;
  }
  .card {
    position: absolute;
    top: 240px;
    height: 720px;
    overflow: hidden;
    border-radius: 74px 0 74px 0;
  }

  /* Front */
  .card-front {
    left: 101px;
    width: 528px;
    background: var(--card-dark);
  }
  .brand {
    position: absolute;
    left: 53px;
    top: 384px;
    display: flex;
    align-items: center;
    gap: 16px;
  }
  .brand-square {
    width: 46px;
    height: 46px;
    background: var(--accent-light);
  }
  .brand-text {
    display: flex;
    flex-direction: column;
  }
  .brand-name {
    font-family: "Questrial", sans-serif;
    color: var(--accent-light);
    font-size: 42px;
    letter-spacing: 2px;
    line-height: 1;
  }
  .brand-tagline {
    font-family: "Questrial", sans-serif;
    color: var(--accent-light);
    font-size: 14px;
    letter-spacing: 4px;
    margin-top: 4px;
  }
  .front-decoration {
    position: absolute;
    left: 0;
    top: 324px;
    width: 528px;
    height: 396px;
    background: linear-gradient(180deg, var(--deco-top) 0%, #7a7a7a 45%, var(--deco-bottom) 100%);
    opacity: 0.9;
  }

  /* Back */
  .card-back {
    left: 672px;
    width: 427px;
    background: var(--card-light);
  }
  .contact {
    position: absolute;
    right: 43px;
    top: 160px;
    text-align: right;
    font-family: "Lato", sans-serif;
    color: var(--ink-soft);
    font-size: 17px;
    line-height: 24px;
  }
  .contact-name {
    font-family: "Questrial", sans-serif;
    color: var(--ink);
    font-size: 23px;
    letter-spacing: 0.5px;
    text-decoration: underline;
    text-underline-offset: 3px;
    line-height: 28px;
  }
  .contact-block { margin: 0; }
  .contact-block + .contact-block { margin-top: 31px; }
  .back-band {
    position: absolute;
    left: 0;
    bottom: 0;
    width: 427px;
    height: 240px;
    background: var(--card-dark);
    display: flex;
    align-items: center;
    justify-content: center;
    gap: 14px;
  }
  .band-square {
    width: 34px;
    height: 34px;
    background: var(--accent-light);
  }
  .band-name {
    font-family: "Questrial", sans-serif;
    color: var(--accent-light);
    font-size: 34px;
    letter-spacing: 2px;
  }
</style>
</head>
<body>
<main class="canvas">
  <section class="card card-front">
    <div class="front-decoration" role="img" aria-label="Área decorativa em tons de cinza da marca"></div>
    <div class="brand">
      <div class="brand-square"></div>
      <div class="brand-text">
        <span class="brand-name">LAR TRAÇO</span>
        <span class="brand-tagline">Projetos &amp; Serviços</span>
      </div>
    </div>
  </section>

  <section class="card card-back">
    <div class="contact">
      <p class="contact-block">
        <span class="contact-name">MARINA TEIXEIRA LOPES</span><br>
        CAU - 41.872-3
      </p>
      <p class="contact-block">
        0xx(93)9000-1234<br>
        marina.projetos@exemplo.com
      </p>
      <p class="contact-block">
        Tv. das Palmeiras, 208-B - Jardim Azul<br>
        Santarém - PA - CEP 68.000-000
      </p>
    </div>
    <div class="back-band">
      <div class="band-square"></div>
      <span class="band-name">LAR TRAÇO</span>
    </div>
  </section>
</main>
</body>
</html>
```